Business Card Design needed for logo design project

Our company needs a Business Card Design. Please refer to our original project in the link above.
Dorian Whitlock
Broker

W: Grandvistaestates.com
P: 214-555-0187
F: 267-555-0142
E: dorianwhitlock@ferncrestmail.com
A: North Dallas Office

Name Spelling update , sorry Dorian Whitlock card is double sided

```html
<!DOCTYPE html>
<html lang="en">
<head>
<meta charset="utf-8">
<title>Grand Vista Realty – Business Card</title>
<link rel="stylesheet" href="https://fonts.googleapis.com/css2?family=EB+Garamond:wght@400;500&display=swap">
<style>
  :root {
    --bg: #5a5a5a;
    --card: #ffffff;
    --gold: #b08f5c;
    --green: #2aa866;
    --ink: #3a3a3a;
    --shadow: rgba(0,0,0,0.35);
  }
  * { margin: 0; padding: 0; box-sizing: border-box; }
  html, body { width: 1200px; height: 1023px; overflow: hidden; }
  body {
    background: var(--bg);
    font-family: "EB Garamond", Georgia, serif;
    position: relative;
  }
  .card {
    position: absolute;
    background: var(--card);
    box-shadow: 0 10px 30px var(--shadow);
  }
  .card-front {
    left: 80px; top: 150px;
    width: 560px; height: 320px;
    display: flex; align-items: center; justify-content: center;
  }
  .card-back {
    left: 720px; top: 230px;
    width: 360px; height: 630px;
    display: flex; flex-direction: column; align-items: center;
    padding-top: 70px;
  }
  .brand {
    display: flex; align-items: center; gap: 14px;
  }
  .brand-mark {
    width: 22px; height: 22px; border-radius: 50%;
    background: var(--gold);
  }
  .brand-name {
    color: var(--gold);
    font-weight: 500;
    letter-spacing: 0.12em;
    text-transform: uppercase;
  }
  .card-front .brand-name { font-size: 34px; }
  .card-back .brand-name { font-size: 22px; }
  .card-back .brand-mark { width: 16px; height: 16px; }
  .agent { margin-top: 120px; text-align: center; }
  .agent-name { font-size: 36px; color: var(--ink); font-weight: 400; }
  .agent-role { font-size: 28px; color: var(--green); }
  .contact-list {
    list-style: none;
    margin-top: 60px;
    font-size: 19px; color: var(--ink);
    display: flex; flex-direction: column; align-items: center; gap: 6px;
  }
  .contact-list li { display: flex; align-items: center; gap: 8px; }
  .contact-icon { width: 14px; height: 14px; flex: none; }
</style>
</head>
<body>
  <section class="card card-front" aria-label="Card front">
    <div class="brand">
      <span class="brand-mark"></span>
      <span class="brand-name">Grand Vista Realty</span>
    </div>
  </section>

  <section class="card card-back" aria-label="Card back">
    <div class="brand">
      <span class="brand-mark"></span>
      <span class="brand-name">Grand Vista Realty</span>
    </div>

    <div class="agent">
      <h1 class="agent-name">Dorian Whitlock</h1>
      <p class="agent-role">Broker</p>
    </div>

    <ul class="contact-list">
      <li>
        <svg class="contact-icon" viewBox="0 0 14 14"><rect x="4" y="1" width="6" height="12" rx="1" fill="none" stroke="#b08f5c" stroke-width="1.3"/></svg>
        214-555-0187
      </li>
      <li>
        <svg class="contact-icon" viewBox="0 0 14 14"><rect x="1" y="5" width="12" height="7" rx="1" fill="#b08f5c"/><rect x="3" y="2" width="8" height="4" fill="none" stroke="#b08f5c" stroke-width="1.2"/></svg>
        267-555-0142
      </li>
      <li>
        <svg class="contact-icon" viewBox="0 0 14 14"><rect x="1" y="3" width="12" height="8" fill="#b08f5c"/><path d="M1 3 L7 8 L13 3" fill="none" stroke="#fff" stroke-width="1"/></svg>
        dorianwhitlock@ferncrestmail.com
      </li>
      <li>
        <svg class="contact-icon" viewBox="0 0 14 14"><circle cx="7" cy="7" r="5.5" fill="none" stroke="#b08f5c" stroke-width="1.2"/><ellipse cx="7" cy="7" rx="2.4" ry="5.5" fill="none" stroke="#b08f5c" stroke-width="1"/><line x1="1.5" y1="7" x2="12.5" y2="7" stroke="#b08f5c" stroke-width="1"/></svg>
        Grandvistaestates.com
      </li>
    </ul>
  </section>
</body>
</html>
```